Cover for "ROOTED! The skill and rhythm of guiding teams through calm and delight"

My first book for a global audience of modern performance leaders needs its cover!
I am an international executive coach and I've developed a new approach to replace classic Performance Management with a natural, sustainable approach fit for human beings :) My first book is about this approach and serves two purposes: helping leaders and sparking their curiosity to learn more, and positioning myself as a thought leader in the field.
The book is built on personal experience; it is both professional and personal ("From me to You"), and I'd like to position it beyond classic categorisation.
Its cover should communicate humanness, naturalness, ease and joy, within an unmistakably business-y context. I would like to see designs that use the color yellow (but not sure it communicates the right things).
Updates

Target Market(s)

Leaders who aspire to have a positive impact and deliver results in a meaningful way

Industry/Entity Type

Consulting & Executive Coaching - Trusted Advisor

Font styles to use
Other font styles liked:
• Helvetica Neue

Colors
0094D4
00A9DD
6FCCEA
C7EBF8
E9F6FB
FFC000
F8CF3A
FAE287
FDF2CF
FEFAEE
EE7325
F08F49
F5BC92
FAE3D3
FDF4ED

Requirements
Must have
• A both-and feeling to it (see description), e.g., masculine AND feminine, business AND humanness. Power with, not power over...
Should not have
• Too much "bling" - no classic status symbol business success language

```html
<!DOCTYPE html>
<html lang="en">
<head>
<meta charset="utf-8">
<title>ROOTED! – Book Cover</title>
<link href="https://fonts.googleapis.com/css2?family=Archivo:wght@900&family=Arimo:wght@400;700&display=swap" rel="stylesheet">
<style>
  :root {
    --stage-grey: #d2d2d2;
    --stage-grey-light: #dedede;
    --paper: #ffffff;
    --rust: #c85a26;
    --ink: #111111;
    --gold: #f6d456;
    --sky-pale: #fff5ba;
    --sky-warm: #fde58a;
    --amber: #f3a93c;
    --ember: #c24c1c;
    --rock: #3a0606;
  }
  html, body {
    margin: 0;
    padding: 0;
    width: 1200px;
    height: 3066px;
    overflow: hidden;
    background: var(--paper);
  }
  .canvas {
    position: relative;
    width: 1200px;
    height: 3066px;
    overflow: hidden;
  }
  .stage {
    position: absolute;
    left: 0;
    width: 1200px;
    background: linear-gradient(180deg, var(--stage-grey-light), var(--stage-grey) 70%, var(--stage-grey-light));
  }
  .stage--pair { top: 0; height: 1125px; }
  .stage--front { top: 1128px; height: 1017px; }
  .stage--spread { top: 2145px; height: 921px; background: var(--paper); }

  .cover {
    position: absolute;
    overflow: hidden;
    box-shadow: 0 10px 24px rgba(0,0,0,0.18);
  }
  .cover__art {
    position: absolute;
    inset: 0;
  }
  .cover--front .cover__art {
    background: linear-gradient(180deg, var(--sky-pale) 0%, var(--sky-warm) 30%, var(--amber) 52%, var(--ember) 70%, var(--rock) 100%);
  }
  .cover--back .cover__art {
    background: linear-gradient(180deg, var(--sky-pale) 0%, var(--sky-warm) 22%, #f7c23e 45%, #e8962e 65%, #a85a1c 100%);
  }
  .cover__head {
    position: absolute;
    top: 4.3em;
    left: 0;
    width: 100%;
    text-align: center;
  }
  .cover__title {
    margin: 0;
    font-family: "Archivo", "Arial Black", sans-serif;
    font-weight: 900;
    font-size: 7.6em;
    line-height: 1;
    letter-spacing: -0.045em;
    color: var(--rust);
  }
  .cover__subtitle {
    margin: 0.45em 0 0;
    font-family: "Arimo", "Helvetica Neue", Arial, sans-serif;
    font-weight: 400;
    font-size: 1.7em;
    line-height: 1.3;
    color: var(--ink);
    text-transform: uppercase;
  }
  .cover--back .cover__head { top: 3.3em; }
  .cover--back .cover__title { font-size: 5.6em; }
  .cover--back .cover__subtitle { font-size: 1.3em; }

  .cover__author {
    position: absolute;
    top: 61em;
    left: 0;
    width: 100%;
    text-align: center;
  }
  .cover__author-name {
    margin: 0;
    font-family: "Arimo", "Helvetica Neue", Arial, sans-serif;
    font-weight: 700;
    font-size: 3.7em;
    line-height: 1.18;
    color: var(--gold);
  }
  .cover__barcode-area {
    position: absolute;
    left: 26.5em;
    top: 62.5em;
    width: 18em;
    height: 8.2em;
    background: var(--paper);
  }

  /* placements */
  .cover--pair-front { left: 110px; top: 200px; width: 440px; height: 657px; font-size: 8.95px; }
  .cover--pair-back  { left: 650px; top: 200px; width: 440px; height: 657px; font-size: 8.95px; }
  .cover--single     { left: 354px; top: 118px; width: 492px; height: 736px; font-size: 10px; }

  .spread {
    position: absolute;
    left: 49px;
    top: 75px;
    width: 1106px;
    height: 797px;
    overflow: hidden;
  }
  .spread .cover { box-shadow: none; top: 0; height: 797px; font-size: 10.84px; }
  .spread .cover--back { left: 0; width: 522px; }
  .spread .cover--front { left: 582px; width: 524px; }

  .spine {
    position: absolute;
    left: 522px;
    top: 0;
    width: 60px;
    height: 797px;
    background: linear-gradient(180deg, var(--sky-pale) 0%, var(--sky-warm) 30%, var(--amber) 55%, var(--ember) 72%, var(--rock) 100%);
  }
  .spine__line {
    position: absolute;
    left: 50%;
    top: 50%;
    width: 797px;
    height: 60px;
    transform: translate(-50%, -50%) rotate(-90deg);
    display: flex;
    align-items: center;
    padding-left: 42px;
    box-sizing: border-box;
    font-family: "Arimo", "Helvetica Neue", Arial, sans-serif;
  }
  .spine__author {
    font-weight: 700;
    font-size: 21px;
    color: var(--gold);
    white-space: nowrap;
  }
  .spine__title {
    margin-left: 92px;
    font-family: "Archivo", "Arial Black", sans-serif;
    font-weight: 900;
    font-size: 28px;
    letter-spacing: -0.03em;
    color: var(--ink);
    white-space: nowrap;
  }
  .spine__subtitle {
    margin-left: 22px;
    font-size: 14px;
    line-height: 1.2;
    color: var(--ink);
    text-transform: uppercase;
    white-space: nowrap;
  }
  .stage-divider {
    position: absolute;
    left: 0;
    top: 1125px;
    width: 1200px;
    height: 3px;
    background: var(--paper);
  }
</style>
</head>
<body>
<main class="canvas">

  <section class="stage stage--pair">
    <article class="cover cover--front cover--pair-front">
      <div class="cover__art" role="img" aria-label="Photo: a person with raised arms standing on a dark rocky summit above golden sunlit mountains"></div>
      <header class="cover__head">
        <h1 class="cover__title">ROOTED!</h1>
        <p class="cover__subtitle">The skill and rhythm of guiding<br>teams through calm and delight</p>
      </header>
      <div class="cover__author"><p class="cover__author-name">AUTHOR<br>NAME</p></div>
    </article>
    <article class="cover cover--back cover--pair-back">
      <div class="cover__art" role="img" aria-label="Photo: golden hazy sky over a mirrored range of sunlit mountains"></div>
      <header class="cover__head">
        <h2 class="cover__title">ROOTED!</h2>
        <p class="cover__subtitle">The skill and rhythm of guiding<br>teams through calm and delight</p>
      </header>
      <div class="cover__barcode-area"></div>
    </article>
  </section>

  <div class="stage-divider"></div>

  <section class="stage stage--front">
    <article class="cover cover--front cover--single">
      <div class="cover__art" role="img" aria-label="Photo: a person with raised arms standing on a dark rocky summit above golden sunlit mountains"></div>
      <header class="cover__head">
        <h2 class="cover__title">ROOTED!</h2>
        <p class="cover__subtitle">The skill and rhythm of guiding<br>teams through calm and delight</p>
      </header>
      <div class="cover__author"><p class="cover__author-name">AUTHOR<br>NAME</p></div>
    </article>
  </section>

  <section class="stage stage--spread">
    <div class="spread">
      <article class="cover cover--back">
        <div class="cover__art" role="img" aria-label="Photo: golden hazy sky over a mirrored range of sunlit mountains"></div>
        <header class="cover__head">
          <h2 class="cover__title">ROOTED!</h2>
          <p class="cover__subtitle">The skill and rhythm of guiding<br>teams through calm and delight</p>
        </header>
        <div class="cover__barcode-area"></div>
      </article>
      <div class="spine">
        <div class="spine__line">
          <span class="spine__author">AUTHOR NAME</span>
          <span class="spine__title">ROOTED!</span>
          <span class="spine__subtitle">The skill and rhythm of guiding<br>teams through calm and delight</span>
        </div>
      </div>
      <article class="cover cover--front">
        <div class="cover__art" role="img" aria-label="Photo: a person with raised arms standing on a dark rocky summit above golden sunlit mountains"></div>
        <header class="cover__head">
          <h2 class="cover__title">ROOTED!</h2>
          <p class="cover__subtitle">The skill and rhythm of guiding<br>teams through calm and delight</p>
        </header>
        <div class="cover__author"><p class="cover__author-name">AUTHOR<br>NAME</p></div>
      </article>
    </div>
  </section>

</main>
</body>
</html>
```